Website design for an events management company

What we need is the design of a website to be used by an events management company, the company is called "Vanto Events Management" and the website is expected to contain the following sections:
1) Homepage
2) Who are we?
3) Mission / Vision / Core values
4) Why to choose Vanto?
5) Past experience
6) Duties or provided services (Scientific Program Duties, Accreditation, Fund Raising, Accommodations, Social Activities, Transportation, Marketing of the Event, Publications and printed materials, Secretarial Work and Media Coverage)
7) References
8) Contact Us page (will probably contain a contact us form plus email, address and a google map)

Attached for your reference the company's logo

Expected that the winner should deliver the designs of at least two pages (the homepage plus an inner page) plus of course all the used graphics, images ... etc.

Thanks

Target Market(s)

The design need to target scientific events and not public events, for example the company doesn't organize music concerts ... etc., it organizes only scientific events so please target business users (i.e. doctors, engineers, scientisits ... etc) while making the designs, including the correct colors, images and icons

Industry/Entity Type

It Company

Number of Pages Required

2 page

Requirements
Must have
• One homepage
• One inner page
• All the used graphics and images
Nice to have
• More than two pages

```html
<!DOCTYPE html>
<html lang="en">
<head>
<meta charset="utf-8">
<title>Vanto Events Management</title>
<link href="https://fonts.googleapis.com/css2?family=Raleway:wght@500;600&family=Open+Sans:wght@400;600&display=swap" rel="stylesheet">
<style>
:root{
  --white:#ffffff;
  --ink:#3d3d3d;
  --muted:#6f6f6f;
  --nav-top:#7a7a7c;
  --nav-bottom:#58585a;
  --nav-divider:#8b8b8d;
  --home-red:#e8413a;
  --pink:#c940b9;
  --orange:#f7931e;
  --green:#7cc143;
  --red:#e53935;
  --purple:#5e2a8c;
  --magenta:#c03fb5;
  --cyan:#29a8e0;
  --leaf-green:#6abf3b;
  --yellow:#f5c518;
  --card-border:#d2d2d2;
  --footer:#6b6b6d;
  --footer-bottom:#58585a;
  --footer-text:#e6e6e6;
  --submit:#12b5d6;
  --field:#f2f2f2;
}
*{box-sizing:border-box;margin:0;padding:0}
html,body{width:820px;height:1200px;overflow:hidden;background:var(--white)}
body{position:relative;font-family:"Open Sans",Arial,sans-serif;color:var(--ink)}

.site-header{position:absolute;left:0;top:0;width:820px;height:88px}
.brand{position:absolute;left:95px;top:24px;display:flex;align-items:center;gap:8px}
.brand-dot{width:22px;height:22px;border-radius:50%;background:var(--purple)}
.brand-name{font-family:"Raleway",sans-serif;font-weight:600;font-size:26px;color:var(--purple);line-height:1}
.brand-tag{position:absolute;left:95px;top:67px;font-size:7.5px;color:var(--muted)}
.header-contact{position:absolute;right:92px;top:30px;text-align:right;font-size:11px;color:var(--ink);line-height:17px}
.header-contact .title{font-size:11.5px}
.header-contact .line{display:flex;justify-content:flex-end;align-items:center;gap:3px}
.header-contact .email{font-size:8.5px}

.main-nav{position:absolute;left:0;top:88px;width:820px;height:33px;background:linear-gradient(var(--nav-top),var(--nav-bottom))}
.main-nav ul{list-style:none;display:flex;position:absolute;left:90px;top:0;height:33px}
.main-nav li{height:33px;line-height:33px;padding:0 8px;font-size:10px;color:var(--white);border-right:1px solid var(--nav-divider)}
.main-nav li:last-child{border-right:none}
.main-nav li.active{background:var(--home-red);padding:0 10px}

.hero{position:absolute;left:0;top:121px;width:820px;height:304px;background:linear-gradient(180deg,#d9c6a0 0%,#b48a52 28%,#6e5a3c 52%,#1f5a4a 72%,#c48b4c 100%)}
.hero-curve{position:absolute;left:0;top:0}
.headline{position:absolute;font-family:"Raleway",sans-serif;color:var(--white);font-weight:600}
.headline.pink{left:182px;top:94px;width:246px;height:40px;background:var(--pink);font-size:30px;line-height:40px;text-align:center;letter-spacing:.5px}
.headline.orange{left:428px;top:94px;width:207px;height:40px;background:var(--orange);font-size:30px;line-height:40px;text-align:center;letter-spacing:.5px}
.headline.green{left:244px;top:138px;width:329px;height:31px;background:var(--green);font-size:16px;line-height:31px;text-align:center;letter-spacing:.3px}
.slider-dots{position:absolute;left:382px;top:275px;display:flex;gap:3px}
.slider-dots span{width:12px;height:12px;border-radius:50%;background:var(--white)}
.slider-dots span.on{background:#1f7fc0;border:2px solid var(--white)}

.services{position:absolute;left:94px;top:457px;width:630px;display:grid;grid-template-columns:repeat(4,149px);column-gap:11px;row-gap:10px}
.service-card{height:148px;border:1px solid var(--card-border);border-radius:4px;text-align:center;background:var(--white)}
.service-card svg{display:block;margin:10px auto 0}
.service-title{font-family:"Raleway",sans-serif;font-weight:500;font-size:14px;color:var(--ink);margin-top:9px}
.service-text{font-size:7px;color:var(--muted);line-height:12px;margin-top:5px;padding:0 14px}

.site-footer{position:absolute;left:0;top:962px;width:820px;height:195px;background:var(--footer);color:var(--footer-text)}
.footer-heading{font-family:"Raleway",sans-serif;font-size:11.5px;color:var(--white);letter-spacing:.2px}
.company-col{position:absolute;left:94px;top:36px}
.company-col ul{list-style:none;margin-top:8px}
.company-col li{font-size:8px;line-height:16.2px}
.footer-map{position:absolute;left:203px;top:36px;width:111px;height:90px;background:linear-gradient(135deg,#eeeae2,#dcd6c8)}
.info-col{position:absolute;left:327px;top:38px;font-size:8px;line-height:16px}
.info-col .addr{margin-top:8px}
.info-col .row{display:flex;align-items:center;gap:5px}
.social{display:flex;gap:4px;margin-top:10px}
.social span{width:21px;height:21px;border:1.3px solid var(--white);border-radius:50%}
.form-col{position:absolute;left:464px;top:36px;width:150px}
.field{height:18px;background:var(--field);border:1px solid #cfcfcf;margin-top:3px;font-size:6.5px;color:#777;padding:4px 8px;position:relative}
.field:first-of-type{margin-top:10px}
.field.tall{height:28px}
.field .caret{position:absolute;right:6px;top:5px}
.submit{display:inline-block;margin-top:6px;margin-left:2px;background:var(--submit);color:var(--white);font-size:7.5px;font-weight:600;padding:5px 12px}
.footer-brand{position:absolute;left:632px;top:64px;display:flex;align-items:center;gap:6px}
.footer-brand .dot{width:20px;height:20px;border-radius:50%;border:1.5px solid var(--white)}
.footer-brand .name{font-family:"Raleway",sans-serif;font-weight:600;font-size:28px;color:var(--white);line-height:1}
.footer-brand-tag{position:absolute;left:632px;top:100px;font-size:7.5px;color:var(--footer-text)}

.footer-bottom{position:absolute;left:0;top:1157px;width:820px;height:43px;background:var(--footer-bottom);color:var(--footer-text);font-size:7.5px}
.footer-bottom p{position:absolute;left:99px;top:17px}
</style>
</head>
<body>

<header class="site-header">
  <div class="brand"><span class="brand-dot"></span><span class="brand-name">Vanto</span></div>
  <div class="brand-tag">Vanto Events Management</div>
  <div class="header-contact">
    <div class="title">Contact Us</div>
    <div class="line">
      <svg width="10" height="10" viewBox="0 0 10 10"><path d="M2 1l2 2-1 1.2c.6 1.3 1.5 2.2 2.8 2.8L7 6l2 2-1.4 1.4C4.5 9.2.8 5.5.6 2.4z" fill="#5e2a8c"/></svg>
      <span>(555) 304-7120</span>
    </div>
    <div class="line email">
      <svg width="11" height="8" viewBox="0 0 11 8"><rect width="11" height="8" rx="1" fill="#5e2a8c"/><path d="M.5 .8l5 3.6 5-3.6" stroke="#fff" fill="none" stroke-width=".9"/></svg>
      <span>hello@vantoevents.com</span>
    </div>
  </div>
</header>

<nav class="main-nav">
  <ul>
    <li class="active">Home</li><li>Who are we</li><li>Mission</li><li>Vision</li><li>Why to choose Vanto?</li><li>Past experience</li><li>Services</li><li>References</li><li>Contact us</li>
  </ul>
</nav>

<section class="hero" role="img" aria-label="Photo of a conference hall with rows of green-clothed tables and gold-covered chairs">
  <div class="headline pink">ESTABLISHING</div>
  <div class="headline orange">LONG-TERM</div>
  <div class="headline green">RELATIONS WITH OUR CUSTOMERS</div>
  <div class="slider-dots"><span class="on"></span><span></span><span></span><span></span></div>
  <svg class="hero-curve" width="820" height="304" viewBox="0 0 820 304"><path d="M0 271 Q410 335 820 271 V304 H0 Z" fill="#fff"/></svg>
</section>

<main class="services">
  <article class="service-card">
    <svg width="56" height="56" viewBox="0 0 56 56"><circle cx="28" cy="28" r="26.5" fill="none" stroke="var(--red)" stroke-width="1.3"/><path d="M18 17h9l-1 8a3.5 3.5 0 0 1-7 0z M30 19l8 3-3 7a3.5 3.5 0 0 1-6-2z" fill="var(--red)"/><path d="M22.5 28v9h-3h6M32 31l-3 8" stroke="var(--red)" stroke-width="1.6" fill="none"/></svg>
    <h3 class="service-title">Our Service</h3>
    <p class="service-text">Curabitur metus ipsum luctus eu malesuada ut tincidunt sed diam Donec quis mi sed magna</p>
  </article>
  <article class="service-card">
    <svg width="56" height="56" viewBox="0 0 56 56"><circle cx="28" cy="28" r="26.5" fill="none" stroke="var(--orange)" stroke-width="1.3"/><rect x="15" y="17" width="26" height="22" rx="2" fill="none" stroke="var(--orange)" stroke-width="1.6"/><rect x="15" y="17" width="26" height="5" fill="var(--orange)"/><g fill="var(--orange)"><rect x="18" y="25" width="3" height="3"/><rect x="23" y="25" width="3" height="3"/><rect x="28" y="25" width="3" height="3"/><rect x="33" y="25" width="3" height="3"/><rect x="18" y="31" width="3" height="3"/><rect x="23" y="31" width="3" height="3"/><rect x="28" y="31" width="3" height="3"/></g></svg>
    <h3 class="service-title">Our Service</h3>
    <p class="service-text">Curabitur metus ipsum luctus eu malesuada ut tincidunt sed diam Donec quis mi sed magna</p>
  </article>
  <article class="service-card">
    <svg width="56" height="56" viewBox="0 0 56 56"><circle cx="28" cy="28" r="26.5" fill="none" stroke="var(--purple)" stroke-width="1.3"/><ellipse cx="28" cy="24" rx="9" ry="10" fill="none" stroke="var(--purple)" stroke-width="1.6"/><path d="M28 34l-1.5 2h3zM28 36c-2 3 2 5 0 8" stroke="var(--purple)" stroke-width="1.3" fill="none"/></svg>
    <h3 class="service-title">Our Service</h3>
    <p class="service-text">Curabitur metus ipsum luctus eu malesuada ut tincidunt sed diam Donec quis mi sed magna</p>
  </article>
  <article class="service-card">
    <svg width="56" height="56" viewBox="0 0 56 56"><circle cx="28" cy="28" r="26.5" fill="none" stroke="var(--magenta)" stroke-width="1.3"/><g fill="var(--magenta)"><circle cx="20" cy="22" r="3.5"/><circle cx="36" cy="22" r="3.5"/><circle cx="28" cy="20" r="4.5"/><path d="M14 35a6 6 0 0 1 12 0zM30 35a6 6 0 0 1 12 0zM20 37a8 8 0 0 1 16 0z"/></g></svg>
    <h3 class="service-title">Our Service</h3>
    <p class="service-text">Curabitur metus ipsum luctus eu malesuada ut tincidunt sed diam Donec quis mi sed magna</p>
  </article>

  <article class="service-card">
    <svg width="56" height="56" viewBox="0 0 56 56"><circle cx="28" cy="28" r="26.5" fill="none" stroke="var(--cyan)" stroke-width="1.3"/><path d="M17 17h22l-9 11v8h5v3H21v-3h5v-8z" fill="var(--cyan)"/></svg>
    <h3 class="service-title">Our Service</h3>
    <p class="service-text">Curabitur metus ipsum luctus eu malesuada ut tincidunt sed diam Donec quis mi sed magna</p>
  </article>
  <article class="service-card">
    <svg width="56" height="56" viewBox="0 0 56 56"><circle cx="28" cy="28" r="26.5" fill="none" stroke="var(--leaf-green)" stroke-width="1.3"/><path d="M38 17c-7 0-12 4-15 10l6 6c6-3 10-8 9-16zM23 27l-5 1-2 3 5 1zM29 33l-1 5-3 2-1-5zM21 33l2 2-5 3z" fill="var(--leaf-green)"/></svg>
    <h3 class="service-title">Our Service</h3>
    <p class="service-text">Curabitur metus ipsum luctus eu malesuada ut tincidunt sed diam Donec quis mi sed magna</p>
  </article>
  <article class="service-card">
    <svg width="56" height="56" viewBox="0 0 56 56"><circle cx="28" cy="28" r="26.5" fill="none" stroke="var(--yellow)" stroke-width="1.3"/><path d="M15 20h16v14H15zM31 24h6l4 5v5H31z" fill="var(--yellow)"/><circle cx="20" cy="35" r="3" fill="#fff" stroke="var(--yellow)" stroke-width="1.5"/><circle cx="36" cy="35" r="3" fill="#fff" stroke="var(--yellow)" stroke-width="1.5"/></svg>
    <h3 class="service-title">Our Service</h3>
    <p class="service-text">Curabitur metus ipsum luctus eu malesuada ut tincidunt sed diam Donec quis mi sed magna</p>
  </article>
  <article class="service-card">
    <svg width="56" height="56" viewBox="0 0 56 56"><circle cx="28" cy="28" r="26.5" fill="none" stroke="var(--orange)" stroke-width="1.3"/><g fill="var(--orange)"><ellipse cx="28" cy="19" rx="3" ry="5"/><ellipse cx="22" cy="25" rx="5" ry="3"/><ellipse cx="34" cy="25" rx="5" ry="3"/><ellipse cx="23" cy="31" rx="4" ry="2.5"/><ellipse cx="33" cy="31" rx="4" ry="2.5"/><rect x="27" y="22" width="2" height="16"/></g></svg>
    <h3 class="service-title">Our Service</h3>
    <p class="service-text">Curabitur metus ipsum luctus eu malesuada ut tincidunt sed diam Donec quis mi sed magna</p>
  </article>

  <article class="service-card">
    <svg width="56" height="56" viewBox="0 0 56 56"><circle cx="28" cy="28" r="26.5" fill="none" stroke="var(--red)" stroke-width="1.3"/><g fill="var(--red)"><rect x="17" y="22" width="22" height="5"/><rect x="19" y="28" width="18" height="10"/><path d="M28 22c-3-5-8-4-6-1zM28 22c3-5 8-4 6-1z"/></g><rect x="26.5" y="22" width="3" height="16" fill="#fff"/></svg>
    <h3 class="service-title">Our Service</h3>
    <p class="service-text">Curabitur metus ipsum luctus eu malesuada ut tincidunt sed diam Donec quis mi sed magna</p>
  </article>
  <article class="service-card">
    <svg width="56" height="56" viewBox="0 0 56 56"><circle cx="28" cy="28" r="26.5" fill="none" stroke="var(--orange)" stroke-width="1.3"/><g fill="var(--orange)"><rect x="24" y="15" width="8" height="7"/><rect x="16" y="31" width="7" height="7"/><rect x="24.5" y="31" width="7" height="7"/><rect x="33" y="31" width="7" height="7"/></g><path d="M28 22v9M19.5 31v-4h17v4" stroke="var(--orange)" stroke-width="1.5" fill="none"/></svg>
    <h3 class="service-title">Our Service</h3>
    <p class="service-text">Curabitur metus ipsum luctus eu malesuada ut tincidunt sed diam Donec quis mi sed magna</p>
  </article>
  <article class="service-card">
    <svg width="56" height="56" viewBox="0 0 56 56"><circle cx="28" cy="28" r="26.5" fill="none" stroke="var(--purple)" stroke-width="1.3"/><path d="M16 21h6l2-3h8l2 3h6v16H16z" fill="var(--purple)"/><circle cx="28" cy="29" r="4.5" fill="none" stroke="#fff" stroke-width="2"/></svg>
    <h3 class="service-title">Our Service</h3>
    <p class="service-text">Curabitur metus ipsum luctus eu malesuada ut tincidunt sed diam Donec quis mi sed magna</p>
  </article>
  <article class="service-card">
    <svg width="56" height="56" viewBox="0 0 56 56"><circle cx="28" cy="28" r="26.5" fill="none" stroke="var(--magenta)" stroke-width="1.3"/><circle cx="23" cy="23" r="6" fill="none" stroke="var(--magenta)" stroke-width="2.5"/><path d="M27 27l11 11M33 33l3-3M36 36l3-3" stroke="var(--magenta)" stroke-width="2.5" fill="none"/></svg>
    <h3 class="service-title">Our Service</h3>
    <p class="service-text">Curabitur metus ipsum luctus eu malesuada ut tincidunt sed diam Donec quis mi sed magna</p>
  </article>
</main>

<footer class="site-footer">
  <div class="company-col">
    <h4 class="footer-heading">COMPANY</h4>
    <ul><li>Who are we</li><li>Mission</li><li>Vision</li><li>Why to choose Vanto?</li><li>Services</li><li>References</li><li>Contact us</li></ul>
  </div>
  <div class="footer-map" role="img" aria-label="Street map showing the office location"></div>
  <div class="info-col">
    <h4 class="footer-heading">CONTACT INFO</h4>
    <p class="addr">410 Harbor Point Avenue, Suite 12</p>
    <p>Fairview, ST 40218</p>
    <p class="row" style="margin-top:5px"><svg width="9" height="9" viewBox="0 0 10 10"><path d="M2 1l2 2-1 1.2c.6 1.3 1.5 2.2 2.8 2.8L7 6l2 2-1.4 1.4C4.5 9.2.8 5.5.6 2.4z" fill="none" stroke="#fff" stroke-width=".9"/></svg>(555) 304-7120</p>
    <p class="row"><svg width="10" height="7" viewBox="0 0 11 8"><rect width="11" height="8" rx="1" fill="#fff"/><path d="M.5 .8l5 3.6 5-3.6" stroke="#6b6b6d" fill="none" stroke-width=".9"/></svg>hello@vantoevents.com</p>
    <div class="social"><span></span><span></span><span></span><span></span></div>
  </div>
  <div class="form-col">
    <h4 class="footer-heading">CONTACT FORM</h4>
    <div class="field">Name</div>
    <div class="field">Email</div>
    <div class="field">Title<svg class="caret" width="8" height="5" viewBox="0 0 8 5"><path d="M.5.5L4 4 7.5.5" stroke="#777" fill="none"/></svg></div>
    <div class="field tall">Message</div>
    <span class="submit">SUBMIT</span>
  </div>
  <div class="footer-brand"><span class="dot"></span><span class="name">Vanto</span></div>
  <div class="footer-brand-tag">Vanto Conference Organizers</div>
</footer>
<div class="footer-bottom"><p>© 2016 Company Name &nbsp;All right reserved &nbsp;Term of Use</p></div>

</body>
</html>
```